Korvesh Menu

Hi there,
My restaurant called "Korvesh" means Spice in hebrew.
We are middle eastern restaurant that specialist in dips,salads and hot bread baked on the spot and charcoal grilled meat skewers
The restaurant is pretty casual and the atmosphere is nice and customers feels like home.
on www.korvesh.com.au you can see photos of the restaurant and the food.
ill add up the menus that i would like to be design please and the logo that is on the front of the shop is been add up
thank you

Target Market(s)

The regulars of the restaurant is jewish/israelis

Industry/Entity Type

Restaurant

```html
<!DOCTYPE html>
<html lang="en">
<head>
<meta charset="utf-8">
<title>Korvesh – Dinner Menu</title>
<link rel="stylesheet" href="https://fonts.googleapis.com/css2?family=Josefin+Sans:wght@400&family=Didact+Gothic&family=Cabin:wght@600&display=swap">
<style>
  :root {
    --ink: #2f2f2f;
    --ink-soft: #777777;
    --rule: #3a3a3a;
    --accent: #c8202f;
    --bullet: #f2b51c;
    --band: #f8e4e6;
    --paper: #ffffff;
  }
  * { box-sizing: border-box; margin: 0; padding: 0; }
  html, body { width: 1200px; height: 800px; overflow: hidden; background: var(--paper); }
  body { font-family: "Didact Gothic", "Helvetica Neue", Arial, sans-serif; color: var(--ink); }

  .menu { width: 1200px; height: 800px; padding: 34px 90px 0; }

  /* Header */
  .menu-header {
    display: flex; align-items: center; justify-content: space-between;
    border-top: 2px solid var(--rule); border-bottom: 2px solid var(--rule);
    padding: 12px 0 10px;
  }
  .menu-title {
    font-family: "Josefin Sans", "Century Gothic", sans-serif;
    font-weight: 400; font-size: 76px; letter-spacing: 14px; line-height: 1;
    padding-top: 8px;
  }
  .venue-details {
    border-left: 2px solid var(--rule); padding: 2px 0 2px 18px;
    font-size: 15px; line-height: 1.4; font-style: normal;
  }
  .venue-name {
    display: block; font-family: "Cabin", "Trebuchet MS", sans-serif; font-weight: 600;
    font-size: 17px; color: var(--accent); letter-spacing: 1px;
  }
  .dot-row {
    height: 32px;
    background-image: radial-gradient(circle, var(--ink) 3px, transparent 3.5px);
    background-size: 78px 32px; background-repeat: repeat-x;
    border-bottom: 2px solid var(--rule);
  }

  /* Sections */
  .menu-section { margin-top: 18px; }
  .section-heading {
    display: flex; align-items: stretch;
    height: 40px; border-top: 2px solid var(--rule); border-bottom: 2px solid var(--rule);
  }
  .section-heading h2 {
    font-family: "Cabin", "Trebuchet MS", sans-serif; font-weight: 600;
    font-size: 24px; color: var(--accent);
    padding-right: 16px; display: flex; align-items: center; gap: 12px; white-space: nowrap;
  }
  .section-heading h2::before {
    content: ""; width: 10px; height: 10px; border-radius: 50%; background: var(--bullet);
  }
  .heading-band { flex: 1; background: var(--band); }

  .section-body { display: grid; grid-template-columns: 1fr 1fr; column-gap: 70px; padding-top: 10px; }
  .item-list { list-style: none; font-size: 20px; line-height: 1.35; }
  .item-list li { display: flex; justify-content: space-between; gap: 12px; }
  .item-list .price { min-width: 70px; text-align: right; }
  .item-list .note { color: var(--ink-soft); }
  .section-note { color: var(--ink-soft); font-size: 17px; line-height: 1.35; margin-top: 4px; }
</style>
</head>
<body>
<main class="menu">
  <header>
    <div class="menu-header">
      <h1 class="menu-title">Dinner Menu</h1>
      <address class="venue-details">
        <span class="venue-name">Korvesh</span>
        412 Marlowe Street,<br>Elsternwick North<br>Tel. 9481 2037
      </address>
    </div>
    <div class="dot-row" aria-hidden="true"></div>
  </header>

  <section class="menu-section">
    <div class="section-heading">
      <h2>Something to start with...</h2>
      <span class="heading-band" role="img" aria-label="Decorative band pattern"></span>
    </div>
    <div class="section-body">
      <ul class="item-list">
        <li><span class="note">Salads &amp; Dips</span><span class="price">$5*</span></li>
        <li><span>6 Falafel Balls</span><span class="price">$8.50</span></li>
        <li><span>Moroccan Beef Cigars</span><span class="price">$9</span></li>
      </ul>
      <ul class="item-list">
        <li><span>Fried Cauliflower</span><span class="price">$8</span></li>
      </ul>
    </div>
  </section>

  <section class="menu-section">
    <div class="section-heading">
      <h2>Salads &amp; Dips...</h2>
      <span class="heading-band" role="img" aria-label="Decorative band pattern"></span>
    </div>
    <div class="section-body">
      <div>
        <ul class="item-list">
          <li><span class="note">3 choices for $12 or 6 choices for $20</span></li>
          <li><span>Baba Ganoush*</span></li>
          <li><span>Matbucha (Moroccan Tomato Salsa)*</span></li>
          <li><span>Chatzilim (Eggplant) *</span></li>
          <li><span>Mira’s Corn Salad *</span></li>
          <li><span>Mixed Pickles *</span></li>
        </ul>
        <p class="section-note">We suggest these if you are looking for a starter<br>or to accompany a Shashlik from the charcoal grill</p>
      </div>
      <ul class="item-list">
        <li><span>Moroccan Carrot *</span></li>
        <li><span>Roasted Beetroot *</span></li>
        <li><span>Hummus*</span></li>
        <li><span>Tahini*</span></li>
      </ul>
    </div>
  </section>

  <section class="menu-section">
    <div class="section-heading">
      <h2>From the charcoal grill...</h2>
      <span class="heading-band" role="img" aria-label="Decorative band pattern"></span>
    </div>
    <div class="section-body">
      <ul class="item-list">
        <li><span>Chicken Shashlik</span><span class="price">$8.50*</span></li>
        <li><span>Lamb Shashlik</span><span class="price">$10*</span></li>
        <li><span>Chatzilim (Eggplant)</span><span class="price">$9*</span></li>
      </ul>
      <ul class="item-list">
        <li><span>Kebab (Kofta) Shashlik</span><span class="price">$9*</span></li>
        <li><span>Chicken Liver</span><span class="price">$8*</span></li>
        <li><span>Mushroom <span class="note">– served with laffa</span></span><span class="price">$8</span></li>
      </ul>
    </div>
  </section>
</main>
</body>
</html>
```